Midwife Poster Ad

I need a poster to go on a wall in my clinic which is in a medical centre shared by doctors and other health professionals. I am a self-employed midwife in New Zealand. I hope for this poster to catch some of the many women who come into the medical centre to have pregnancy tests, see a doctor, or use the pregnancy yoga/pilates services also offered. It will be going on a wall with a bunch of other brochures and ads, so obviously I would like it to stand out and grab their attention as they walk in or out of the centre.

I have attached a few of the images that I currently use in my business cards and brochures. I would like my portrait to feature somewhere on the poster, but does not need to be central. The other images can be used if they work with the design, but are not essential. I would like the poster to include at least one image of a new baby or a pregnant woman/couple.

I would also like a small business card-sized space at the bottom where I can attach a card-holder. I would like the website address to stand out.

The poster should be colourful and communicate the excitement of a new pregnancy.

Target Market(s)

Pregnant women, mothers

Industry/Entity Type

Small Business

Requirements
Must have
• The poster needs to include the following text:
EXPECTING A BABY?
Midwife available here!
Marlene Tobbit LMC Midwife
Clinics run from Kestrel Physio & Pilates
Free pregnancy testing
www.brindlewoodmidwife.co.nz
0215379064

```html
<!DOCTYPE html>
<html lang="en">
<head>
<meta charset="utf-8">
<title>Expecting a Baby? – Midwife Poster</title>
<link rel="stylesheet" href="https://fonts.googleapis.com/css2?family=Bebas+Neue&family=Freckle+Face&family=Sniglet:wght@400;800&display=swap">
<style>
  :root {
    --pink: #f5a8c3;
    --pink-dot: #ffffff;
    --leaf: #e3ecc0;
    --leaf-dot: #dfe8b4;
    --sky: #cfe6ee;
    --cocoa: #6a3832;
    --plum: #8a2f8c;
    --ink: #111111;
    --paper: #ffffff;
  }
  * { margin: 0; padding: 0; box-sizing: border-box; }
  html, body { width: 1000px; height: 1200px; overflow: hidden; background: var(--paper); }
  .poster { position: relative; width: 1000px; height: 1200px; overflow: hidden; background: var(--paper); }

  .strip-top { position: absolute; left: 75px; top: 0; width: 850px; height: 18px; background: var(--leaf); }
  .rule-top { position: absolute; left: 75px; top: 30px; width: 850px; height: 6px; background: var(--sky); }
  .rule-bottom { position: absolute; left: 75px; top: 1163px; width: 850px; height: 6px; background: var(--sky); }
  .strip-bottom { position: absolute; left: 75px; top: 1184px; width: 850px; height: 16px; background: var(--leaf); }

  .photo { position: absolute; }
  .photo--newborn-basket { left: 375px; top: 0; width: 550px; height: 300px;
    background: linear-gradient(135deg, #f1d6c9 0%, #f6f3f1 55%, #d9a27a 100%); }
  .photo--sleeping-baby { left: 75px; top: 585px; width: 238px; height: 228px;
    background: radial-gradient(ellipse at 55% 55%, #efc2aa 0%, #d86a5c 55%, #b31d22 100%); }
  .photo--father-baby { left: 370px; top: 540px; width: 240px; height: 236px;
    background: linear-gradient(160deg, #3a3a3a 0%, #8a8a8a 55%, #cfcfcf 100%); }
  .photo--expecting-couple { left: 690px; top: 505px; width: 235px; height: 232px;
    background: radial-gradient(ellipse at 45% 65%, #c9a08c 0%, #4a3a34 45%, #0d0d0d 100%); }
  .photo--portrait { left: 75px; top: 815px; width: 265px; height: 365px;
    background: linear-gradient(180deg, #fdfdfd 0%, #f3dccd 30%, #e8bfa8 60%, #1d2433 88%); }

  .bands { position: absolute; left: 0; top: 0; width: 1000px; height: 1200px; }

  .headline { position: absolute; left: 75px; top: 288px; width: 850px; text-align: center;
    transform: rotate(-5deg); transform-origin: center; }
  .headline__main { display: block; font-family: "Bebas Neue", sans-serif; font-size: 176px;
    line-height: 0.9; color: var(--paper); letter-spacing: 2px; }
  .headline__sub { display: block; font-family: "Bebas Neue", sans-serif; font-size: 92px;
    line-height: 0.9; color: var(--cocoa); letter-spacing: 2px; }

  .contact { position: absolute; right: 100px; top: 768px; width: 640px; text-align: right;
    transform: rotate(-5deg); transform-origin: right center; }
  .contact__lead { font-family: "Freckle Face", cursive; font-size: 55px; color: var(--plum);
    line-height: 1.1; margin-bottom: 10px; }
  .contact__line { font-family: "Sniglet", sans-serif; font-weight: 800; font-size: 27px; color: var(--ink);
    line-height: 1.2; }
  .contact__web { font-family: "Sniglet", sans-serif; font-size: 28px; color: var(--plum);
    line-height: 1.2; margin-top: 10px; }
  .contact__phone { font-family: "Sniglet", sans-serif; font-weight: 800; font-size: 27px; color: var(--ink);
    line-height: 1.2; }
</style>
</head>
<body>
<main class="poster">
  <div class="strip-top"></div>
  <div class="rule-top"></div>

  <div class="photo photo--newborn-basket" role="img" aria-label="Photo of a newborn baby lying in a woven basket with white blanket"></div>

  <svg class="bands" viewBox="0 0 1000 1200" aria-hidden="true">
    <polygon class="band-leaf" points="75,590 925,490 925,712 75,815" fill="var(--leaf)"/>
    <polygon class="band-pink" points="75,322 925,222 925,500 75,600" fill="var(--pink)"/>
    <line x1="75" y1="322" x2="925" y2="222" stroke="var(--pink-dot)" stroke-width="5" stroke-linecap="round" stroke-dasharray="0 11"/>
    <line x1="75" y1="600" x2="925" y2="500" stroke="var(--pink-dot)" stroke-width="5" stroke-linecap="round" stroke-dasharray="0 11"/>
    <line x1="75" y1="818" x2="925" y2="715" stroke="var(--leaf-dot)" stroke-width="6" stroke-linecap="round" stroke-dasharray="0 13"/>
  </svg>

  <div class="photo photo--sleeping-baby" role="img" aria-label="Photo of a sleeping newborn on a red background"></div>
  <div class="photo photo--father-baby" role="img" aria-label="Black and white photo of a father kissing his newborn baby"></div>
  <div class="photo photo--expecting-couple" role="img" aria-label="Photo of an expecting couple holding the pregnant belly"></div>

  <h1 class="headline">
    <span class="headline__main">EXPECTING</span>
    <span class="headline__sub">A BABY?</span>
  </h1>

  <div class="photo photo--portrait" role="img" aria-label="Portrait of midwife Marlene Tobbit"></div>

  <section class="contact">
    <p class="contact__lead">Midwife available here</p>
    <p class="contact__line">Marlene Tobbit LMC Midwife</p>
    <p class="contact__line">Clinics run from Kestrel Physio &amp; Pilates</p>
    <p class="contact__line">Free pregnancy testing</p>
    <p class="contact__web">www.brindlewoodmidwife.co.nz</p>
    <p class="contact__phone">0215379064</p>
  </section>

  <div class="rule-bottom"></div>
  <div class="strip-bottom"></div>
</main>
</body>
</html>
```